Managed Service Provider need new business cards

We are a small Maanged Service Provider of IT Services and need a new fresh design for our business cards. We want something impossible, fun and professional :)
Our services has a large range, but we are always fun and make sure our customers both get their issue sorted and also feel like they are "catching up with an old friend".
All our cards in the past has always been all black, with red and we need something fresher.
The back of card, we would like just a small list of what we do i think, but if someone has a better idea, please do something cool with the back of the card:
Managed IT Services
Productivity Solutions
Data Backup and Recovery
IT System Maintenance
Managed IT Security
More details can be found on our website tqnetworks.com.au
Industry/Entity Type
It Company
Contact Information for Business Card
Name: Dwayne Falstrup
Title: Director
Phone: 03 6193 4827
Mobile: 0412 587 239
Email: dwayne@tqnetworks.com.au
Web: www.tqnetworks.com.au

```html
<!DOCTYPE html>
<html lang="en">
<head>
<meta charset="utf-8">
<title>TQ Networks — Business Cards</title>
<link href="https://fonts.googleapis.com/css2?family=Montserrat:wght@400;500;700;800&display=swap" rel="stylesheet">
<style>
  :root {
    --stage: #3a3a3c;
    --card-white: #ffffff;
    --brand-red: #d81e2a;
    --brand-red-deep: #a8101a;
    --brand-red-light: #ee3b45;
    --ink-light: #ffffff;
    --edge-shadow: #c9c9c9;
  }
  * { margin: 0; padding: 0; box-sizing: border-box; }
  html, body { width: 1200px; height: 913px; overflow: hidden; }
  body {
    background: var(--stage);
    font-family: "Montserrat", Arial, sans-serif;
    position: relative;
  }
  .card {
    position: absolute;
    left: 320px;
    width: 560px;
    height: 320px;
    background: var(--card-white);
    overflow: hidden;
    box-shadow: 0 10px 30px rgba(0,0,0,.45);
  }
  .card--services { top: 110px; }
  .card--contact { top: 483px; }
  .card__wave { position: absolute; inset: 0; width: 100%; height: 100%; }

  .brand-name {
    position: absolute;
    display: flex;
    align-items: center;
    gap: 9px;
    color: var(--brand-red);
    font-weight: 800;
    font-size: 24px;
    letter-spacing: 1px;
    white-space: nowrap;
  }
  .brand-name__dot {
    width: 14px; height: 14px; border-radius: 50%;
    background: var(--brand-red);
  }
  .card--services .brand-name { left: 30px; top: 150px; }
  .card--contact .brand-name { right: 40px; top: 52px; }

  .services {
    position: absolute;
    right: 34px;
    top: 60px;
    text-align: right;
    color: var(--ink-light);
  }
  .services__title {
    font-weight: 700;
    font-size: 15px;
    letter-spacing: 1px;
    display: flex;
    align-items: center;
    justify-content: flex-end;
    gap: 10px;
    margin-bottom: 12px;
  }
  .services__title::before {
    content: ""; width: 90px; height: 1px; background: rgba(255,255,255,.7);
  }
  .services__list { list-style: none; }
  .services__item {
    font-size: 13px;
    font-weight: 400;
    line-height: 25px;
    display: flex;
    align-items: center;
    justify-content: flex-end;
    gap: 8px;
  }
  .services__item svg { width: 11px; height: 11px; }

  .person {
    position: absolute;
    left: 34px;
    top: 160px;
    color: var(--ink-light);
  }
  .person__role { font-size: 13px; font-weight: 400; }
  .person__rule { width: 130px; height: 1px; background: rgba(255,255,255,.7); margin: 2px 0 3px; }
  .person__name { font-size: 16px; font-weight: 700; letter-spacing: .5px; }
  .person__mobile { font-size: 14px; display: flex; align-items: center; gap: 8px; margin-top: 2px; }

  .contact-list {
    position: absolute;
    left: 34px;
    bottom: 22px;
    list-style: none;
    color: var(--ink-light);
  }
  .contact-list__item {
    font-size: 14px;
    line-height: 24px;
    display: flex;
    align-items: center;
    gap: 8px;
  }
  .contact-list svg, .person__mobile svg { width: 13px; height: 13px; fill: var(--ink-light); }
</style>
</head>
<body>

<section class="card card--services">
  <svg class="card__wave" viewBox="0 0 560 320" preserveAspectRatio="none" aria-hidden="true">
    <defs>
      <linearGradient id="redGlossA" x1="0" y1="0" x2="1" y2="1">
        <stop offset="0" stop-color="var(--brand-red-light)"/>
        <stop offset=".55" stop-color="var(--brand-red)"/>
        <stop offset="1" stop-color="var(--brand-red-deep)"/>
      </linearGradient>
    </defs>
    <path d="M560 0 L330 0 C282 0 302 70 292 120 C282 175 256 220 268 265 C280 305 330 320 390 320 L560 320 Z" fill="var(--edge-shadow)" transform="translate(-4 3)"/>
    <path d="M560 0 L330 0 C282 0 302 70 292 120 C282 175 256 220 268 265 C280 305 330 320 390 320 L560 320 Z" fill="url(#redGlossA)"/>
  </svg>

  <div class="brand-name"><span class="brand-name__dot"></span>TQ NETWORKS</div>

  <div class="services">
    <h2 class="services__title">SERVICES</h2>
    <ul class="services__list">
      <li class="services__item">Managed IT Services <svg viewBox="0 0 12 12"><path d="M1 6.5 L4.5 10 L11 2" fill="none" stroke="#fff" stroke-width="2"/></svg></li>
      <li class="services__item">Productivity Solutions <svg viewBox="0 0 12 12"><path d="M1 6.5 L4.5 10 L11 2" fill="none" stroke="#fff" stroke-width="2"/></svg></li>
      <li class="services__item">Data Backup and Recovery <svg viewBox="0 0 12 12"><path d="M1 6.5 L4.5 10 L11 2" fill="none" stroke="#fff" stroke-width="2"/></svg></li>
      <li class="services__item">IT System Maintenance <svg viewBox="0 0 12 12"><path d="M1 6.5 L4.5 10 L11 2" fill="none" stroke="#fff" stroke-width="2"/></svg></li>
      <li class="services__item">Managed IT Security <svg viewBox="0 0 12 12"><path d="M1 6.5 L4.5 10 L11 2" fill="none" stroke="#fff" stroke-width="2"/></svg></li>
    </ul>
  </div>
</section>

<section class="card card--contact">
  <svg class="card__wave" viewBox="0 0 560 320" preserveAspectRatio="none" aria-hidden="true">
    <defs>
      <linearGradient id="redGlossB" x1="0" y1="0" x2="1" y2="1">
        <stop offset="0" stop-color="var(--brand-red-deep)"/>
        <stop offset=".5" stop-color="var(--brand-red)"/>
        <stop offset="1" stop-color="var(--brand-red-light)"/>
      </linearGradient>
    </defs>
    <path d="M0 320 L0 150 C60 150 70 112 125 112 C200 112 235 158 330 142 C405 128 420 200 450 240 C478 282 515 298 560 298 L560 320 Z" fill="var(--edge-shadow)" transform="translate(3 -4)"/>
    <path d="M0 320 L0 150 C60 150 70 112 125 112 C200 112 235 158 330 142 C405 128 420 200 450 240 C478 282 515 298 560 298 L560 320 Z" fill="url(#redGlossB)"/>
  </svg>

  <div class="brand-name"><span class="brand-name__dot"></span>TQ NETWORKS</div>

  <div class="person">
    <p class="person__role">Director</p>
    <div class="person__rule"></div>
    <p class="person__name">DWAYNE FALSTRUP</p>
    <p class="person__mobile"><svg viewBox="0 0 12 16"><path d="M2 0h8a2 2 0 0 1 2 2v12a2 2 0 0 1-2 2H2a2 2 0 0 1-2-2V2a2 2 0 0 1 2-2zm0 2v10h8V2z"/></svg>0412 587 239</p>
  </div>

  <ul class="contact-list">
    <li class="contact-list__item"><svg viewBox="0 0 16 16"><path d="M3 1l3 3-2 2c1 2 3 4 5 5l2-2 3 3-2 3C7 15 1 9 0 4z"/></svg>03 6193 4827</li>
    <li class="contact-list__item"><svg viewBox="0 0 16 12"><path d="M0 0h16v12H0zM1.5 1.5 8 7l6.5-5.5z" fill-rule="evenodd"/></svg>dwayne@tqnetworks.com.au</li>
    <li class="contact-list__item"><svg viewBox="0 0 16 16"><circle cx="8" cy="8" r="7" fill="none" stroke="#fff" stroke-width="1.5"/><path d="M1 8h14M8 1c3 3 3 11 0 14M8 1c-3 3-3 11 0 14" fill="none" stroke="#fff" stroke-width="1.2"/></svg>www.tqnetworks.com.au</li>
  </ul>
</section>

</body>
</html>
```